Income Tax Flyer - Updates Needed

Just need to update this flyer design and give it a new look. We would like to keep all the same wording but make it stand out a little more. Our selling point is the "Same Day Tax Advance up to $6,000"

Industry/Entity Type

Lending, Small Loans, Tax Services, Title Loans, Personal Loans

```html
<!DOCTYPE html>
<html lang="en">
<head>
<meta charset="utf-8">
<title>Same Day Tax Advance Flyer</title>
<link rel="stylesheet" href="https://fonts.googleapis.com/css2?family=Oswald:wght@600;700&family=Archivo+Black&family=Poppins:wght@500;600;700&display=swap">
<style>
  :root {
    --brand-red: #c8202f;
    --brand-green: #0f5a2e;
    --ink: #1b1b1b;
    --paper: #ffffff;
    --stage: #ffffff;
  }
  html, body {
    margin: 0;
    padding: 0;
    width: 1200px;
    height: 2395px;
    overflow: hidden;
    background: var(--stage);
  }
  .flyer {
    position: absolute;
    left: 80px;
    top: 397px;
    width: 1040px;
    height: 1600px;
    box-shadow: 0 10px 30px rgba(0,0,0,0.18);
    background: var(--paper);
  }
  .flyer svg { display: block; width: 100%; height: 100%; }
  .headline-condensed { font-family: "Oswald", "Arial Narrow", sans-serif; font-weight: 700; }
  .headline-heavy { font-family: "Archivo Black", "Arial Black", sans-serif; }
  .body-text { font-family: "Poppins", "Helvetica", sans-serif; }
  .fill-red { fill: var(--brand-red); }
  .fill-green { fill: var(--brand-green); }
  .fill-ink { fill: var(--ink); }
</style>
</head>
<body>
<div class="flyer">
  <svg viewBox="0 0 754 1160" xmlns="http://www.w3.org/2000/svg">
    <defs>
      <linearGradient id="heroHaze" x1="0" y1="0" x2="0" y2="1">
        <stop offset="0" stop-color="#e3e9e4"/>
        <stop offset="1" stop-color="#f1f2ef"/>
      </linearGradient>
      <linearGradient id="peopleTone" x1="0" y1="0" x2="1" y2="1">
        <stop offset="0" stop-color="#b9a59a"/>
        <stop offset="0.5" stop-color="#4a4f55"/>
        <stop offset="1" stop-color="#6f7b76"/>
      </linearGradient>
    </defs>

    <!-- hero background -->
    <rect class="hero-backdrop" x="0" y="0" width="754" height="660" fill="url(#heroHaze)" role="img" aria-label="Faded office scene with floating banknotes"/>
    <rect class="lower-backdrop" x="0" y="640" width="754" height="520" fill="#f7f7f6" role="img" aria-label="Faint photo of a couple reviewing paperwork"/>

    <!-- couple photo -->
    <rect class="hero-people" x="432" y="115" width="322" height="480" rx="6" fill="url(#peopleTone)" role="img" aria-label="Smiling couple standing with arms crossed"/>

    <!-- headline -->
    <text class="headline-condensed fill-red" x="45" y="128" font-size="104" textLength="342" lengthAdjust="spacingAndGlyphs">$AME DAY</text>
    <text class="headline-heavy fill-green" x="45" y="255" font-size="190" textLength="342" lengthAdjust="spacingAndGlyphs">TAX</text>
    <text class="headline-condensed fill-green" x="45" y="350" font-size="104" textLength="338" lengthAdjust="spacingAndGlyphs">ADVANCE</text>
    <text class="headline-condensed fill-red" x="45" y="525" font-size="154" textLength="378" lengthAdjust="spacingAndGlyphs">$6,000</text>
    <g class="upto-badge">
      <circle cx="215" cy="392" r="28" fill="var(--brand-green)" stroke="#fff" stroke-width="3"/>
      <text class="body-text" x="215" y="389" font-size="15" font-weight="600" fill="#fff" text-anchor="middle">UP</text>
      <text class="body-text" x="215" y="405" font-size="15" font-weight="600" fill="#fff" text-anchor="middle">TO</text>
    </g>

    <!-- swoosh bands -->
    <path class="swoosh-white" d="M0 650 Q330 520 754 630 L754 1160 L0 1160 Z" fill="#fbfbfa"/>
    <path class="swoosh-red" d="M0 650 L0 635 Q330 510 754 600 L754 615 Q330 540 0 650 Z" fill="var(--brand-red)"/>
    <path class="swoosh-green" d="M60 630 Q380 540 754 632 L754 615 Q380 555 60 630 Z" fill="var(--brand-green)"/>

    <!-- tagline -->
    <text class="body-text fill-green" x="377" y="672" font-size="40" font-weight="500" text-anchor="middle" textLength="606" lengthAdjust="spacingAndGlyphs">File your taxes &amp;apply for an</text>
    <text class="body-text fill-red" x="377" y="728" font-size="56" font-weight="700" text-anchor="middle" textLength="505" lengthAdjust="spacingAndGlyphs">EASY ADVANCE!</text>

    <!-- benefits -->
    <g class="benefit benefit-time">
      <circle cx="155" cy="813" r="57" fill="none" stroke="var(--brand-red)" stroke-width="2" stroke-dasharray="9 6"/>
      <circle cx="155" cy="813" r="46" fill="#fff" stroke="var(--brand-red)" stroke-width="6"/>
      <path d="M137 805 A20 20 0 1 1 147 830" fill="none" stroke="var(--brand-green)" stroke-width="4"/>
      <path d="M130 800 L138 812 L146 802 Z" fill="var(--brand-green)"/>
      <path d="M157 795 L157 810 L167 810" fill="none" stroke="var(--brand-green)" stroke-width="3"/>
      <text class="body-text fill-green" x="142" y="833" font-size="13" font-weight="700" text-anchor="middle">24h</text>
      <text class="body-text fill-ink" x="155" y="915" font-size="20" font-weight="500" text-anchor="middle">Available in</text>
      <text class="body-text fill-ink" x="155" y="940" font-size="20" font-weight="500" text-anchor="middle">24 hours</text>
      <text class="body-text fill-ink" x="155" y="965" font-size="20" font-weight="500" text-anchor="middle">or less</text>
    </g>
    <line x1="258" y1="755" x2="258" y2="950" stroke="var(--ink)" stroke-width="2" stroke-dasharray="7 6"/>
    <g class="benefit benefit-amount">
      <circle cx="378" cy="813" r="57" fill="none" stroke="var(--brand-red)" stroke-width="2" stroke-dasharray="9 6"/>
      <circle cx="378" cy="813" r="46" fill="#fff" stroke="var(--brand-green)" stroke-width="6"/>
      <circle cx="381" cy="798" r="14" fill="var(--brand-red)"/>
      <text class="body-text" x="381" y="805" font-size="18" font-weight="700" fill="#fff" text-anchor="middle">$</text>
      <rect x="352" y="818" width="9" height="18" fill="var(--brand-red)"/>
      <path d="M364 820 L390 820 Q404 818 410 812 L413 818 Q402 834 388 836 L364 836 Z" fill="var(--brand-red)"/>
      <text class="body-text fill-ink" x="378" y="915" font-size="20" font-weight="500" text-anchor="middle">choose your</text>
      <text class="body-text fill-ink" x="378" y="940" font-size="20" font-weight="500" text-anchor="middle">loan amount</text>
    </g>
    <line x1="500" y1="755" x2="500" y2="950" stroke="var(--ink)" stroke-width="2" stroke-dasharray="7 6"/>
    <g class="benefit benefit-easy">
      <circle cx="605" cy="813" r="57" fill="none" stroke="var(--brand-red)" stroke-width="2" stroke-dasharray="9 6"/>
      <circle cx="605" cy="813" r="46" fill="#fff" stroke="var(--brand-red)" stroke-width="6"/>
      <rect x="588" y="790" width="34" height="18" rx="2" fill="var(--brand-green)"/>
      <circle cx="605" cy="799" r="5" fill="#fff"/>
      <rect x="584" y="812" width="9" height="18" fill="var(--brand-green)"/>
      <path d="M596 814 L616 814 Q624 812 628 808 L630 814 Q622 828 612 830 L596 830 Z" fill="var(--brand-green)"/>
      <text class="body-text fill-ink" x="605" y="913" font-size="20" font-weight="500" text-anchor="middle">Quick and</text>
      <text class="body-text fill-ink" x="605" y="938" font-size="20" font-weight="500" text-anchor="middle">easy</text>
    </g>

    <!-- brand -->
    <g class="brand-name">
      <circle cx="56" cy="1059" r="11" fill="var(--brand-green)"/>
      <text class="body-text fill-green" x="74" y="1066" font-size="21" font-weight="600" textLength="196" lengthAdjust="spacingAndGlyphs">Keystone Capital</text>
    </g>
    <line x1="295" y1="980" x2="295" y2="1130" stroke="var(--ink)" stroke-width="2"/>

    <!-- contact -->
    <g class="contact">
      <text class="body-text fill-red" x="323" y="1002" font-size="25" font-weight="700">CONTACT US TODAY!</text>
      <g class="icon-phone">
        <circle cx="337" cy="1037" r="12" fill="var(--brand-red)"/>
        <path d="M331 1031 Q331 1045 344 1044 L344 1040 L340 1038 L338 1040 Q334 1038 334 1034 L336 1032 L334 1029 Z" fill="#fff"/>
      </g>
      <text class="body-text fill-ink" x="361" y="1048" font-size="31" font-weight="600">(555) 210-3478</text>
      <g class="icon-pin">
        <path d="M337 1064 a11 11 0 0 1 11 11 c0 8 -11 18 -11 18 c0 0 -11 -10 -11 -18 a11 11 0 0 1 11 -11 Z" fill="var(--brand-red)"/>
        <circle cx="337" cy="1075" r="4" fill="#fff"/>
      </g>
      <text class="body-text fill-green" x="361" y="1082" font-size="19" font-weight="700">Lakeview – North Branch</text>
      <text class="body-text fill-ink" x="361" y="1103" font-size="15" font-weight="500">4150-2 N. Maple Ave,</text>
      <text class="body-text fill-ink" x="361" y="1123" font-size="15" font-weight="500">Lakeview, Texas 78901</text>
    </g>
  </svg>
</div>
</body>
</html>
```